Business card design for event company

need design double sided in square shape ( approx 6x6cm) in matt grey shades
front side :
logo ( could be in one color like picture attached ) printpress effect in a rect box

back side :
name in big font with silver foil finish ( similar to attached pic )

phone number i would like to see how it will look like if embossed ( like in credit cards )

Sample for contact on card ( will need 5 different contacts) - pls. include small icons next to each contact

WALEED RAFIQI
Managing Director

+971 50 317 6490
waleed@loomcrestuae.com
www.loomcrest.ae
Building C2 , Office 713
Dubai Saffron Heights

Please consider this is an urgent project . thank you in advance

```html
<!DOCTYPE html>
<html lang="en">
<head>
<meta charset="utf-8">
<title>Loomcrest — Business Card</title>
<link rel="stylesheet" href="https://fonts.googleapis.com/css2?family=Open+Sans:wght@400;600;700&family=Courier+Prime:wght@700&display=swap">
<style>
  :root {
    --backdrop: #ece9e4;
    --silver-light: #f4f4f4;
    --silver-mid: #c9c9c9;
    --silver-dark: #a9a9a9;
    --orange: #ee8f24;
    --ink-grey: #555555;
    --ink-dark: #1e1e1e;
    --matte-grey: #9b989a;
    --matte-grey-light: #aaa7a9;
    --mark-black: #0a0a0a;
  }
  * { box-sizing: border-box; margin: 0; padding: 0; }
  html, body {
    width: 1200px; height: 1200px; overflow: hidden;
    background: var(--backdrop);
  }
  .canvas { position: relative; width: 1200px; height: 1200px; }

  .card {
    position: absolute; left: 362px; width: 478px; height: 478px;
    overflow: hidden;
    font-family: "Open Sans", Arial, sans-serif;
  }

  /* Front */
  .card--front {
    top: 96px;
    background: linear-gradient(125deg, var(--silver-dark) 0%, var(--silver-light) 28%, var(--silver-mid) 48%, var(--silver-light) 70%, var(--silver-dark) 100%);
  }
  .brand-name {
    position: absolute; top: 62px; left: 0; width: 100%;
    text-align: center;
    font-size: 64px; font-weight: 600; color: var(--ink-grey);
    letter-spacing: 1px;
  }
  .phone-emboss {
    position: absolute; top: 138px; left: 0; width: 100%;
    text-align: center;
    font-family: "Courier Prime", "Courier New", monospace;
    font-weight: 700; font-size: 30px; letter-spacing: 3px;
    color: #2a2a2a;
    text-shadow: 1px 1px 0 rgba(255,255,255,0.7), -1px -1px 0 rgba(0,0,0,0.25);
  }
  .wave { position: absolute; inset: 0; width: 478px; height: 478px; }

  .contact-block { position: absolute; left: 29px; top: 285px; color: var(--ink-dark); }
  .person-name { font-size: 21px; font-weight: 700; line-height: 1.2; }
  .person-title { font-size: 16px; line-height: 1.5; margin-bottom: 12px; }
  .contact-list { list-style: none; font-size: 16px; }
  .contact-list li { display: flex; align-items: center; gap: 3px; line-height: 1.45; }
  .contact-list li.address {
    margin-top: 4px; padding-top: 4px;
    border-top: 1px solid var(--ink-dark);
    width: 340px; letter-spacing: -0.3px;
  }
  .contact-list svg { width: 13px; height: 13px; flex: none; }

  /* Back */
  .card--back {
    top: 634px;
    background: radial-gradient(circle at 40% 30%, var(--matte-grey-light), var(--matte-grey) 70%, #8e8b8d);
    display: flex; align-items: center; justify-content: center;
  }
  .back-name {
    font-size: 34px; font-weight: 700; color: var(--mark-black);
    letter-spacing: 2px;
  }
</style>
</head>
<body>
<div class="canvas">

  <section class="card card--front">
    <div class="brand-name">Loomcrest</div>
    <div class="phone-emboss">+971 50 317 6490</div>

    <svg class="wave" viewBox="0 0 478 478" aria-hidden="true">
      <path d="M0,220 Q40,190 120,192 Q300,200 478,478 L0,478 Z" fill="var(--orange)"/>
      <path d="M0,232 Q45,205 122,206 Q295,214 466,478 L0,478 Z" fill="#f2f2f2"/>
      <path d="M0,240 Q48,214 124,216 Q290,226 458,478 L0,478 Z" fill="var(--orange)"/>
    </svg>

    <div class="contact-block">
      <div class="person-name">WALEED RAFIQI</div>
      <div class="person-title">Managing Director</div>
      <ul class="contact-list">
        <li>
          <svg viewBox="0 0 16 16"><circle cx="8" cy="8" r="7" fill="none" stroke="currentColor" stroke-width="2"/><path d="M1 8h14M8 1c3 3 3 11 0 14M8 1c-3 3-3 11 0 14" fill="none" stroke="currentColor" stroke-width="1.4"/></svg>
          www.loomcrest.ae
        </li>
        <li>
          <svg viewBox="0 0 16 16"><rect x="1" y="3" width="14" height="10" fill="currentColor"/><path d="M1 3l7 6 7-6" fill="none" stroke="var(--orange)" stroke-width="1.4"/></svg>
          waleed@loomcrestuae.com
        </li>
        <li class="address">
          <svg viewBox="0 0 16 16"><path d="M8 1a5 5 0 0 1 5 5c0 4-5 9-5 9S3 10 3 6a5 5 0 0 1 5-5z" fill="currentColor"/><circle cx="8" cy="6" r="2" fill="var(--orange)"/></svg>
          Building C2 , Office 713, Dubai Saffron Heights
        </li>
      </ul>
    </div>
  </section>

  <section class="card card--back">
    <div class="back-name">WALEED RAFIQI</div>
  </section>

</div>
</body>
</html>
```